Finance Company Need Presentation Folder/ Brochure Design

We are a Finance Brokerage Firm in Adelaide, we provide finance for personal, car, equipment, boat and aviation loans. We are looking for designs for new presentation folders that are simplistic, yet professional and classy. We would like them to include the color orange and communicate financial safety and growth.

Target Market(s)

The folders will be going to current and perspective clients

Industry/Entity Type

Finance

Font styles to use
Other font styles liked:
• Raleway or something similar, example attached as 'Open Door Lending Evening'

Colors
f37122
ffffff
000000

Requirements
Must have
• Phone Number: 1300 482 917
• Address:
• 47 Tamsin Road
• Brindlemoor, SA 5092
• Website: kelvarupath.com.au
Nice to have
• "Experience finance in a whole new way... Experience Kelvarupath"
• Asset Finance - Home Loans - Personal Loans

```html
<!DOCTYPE html>
<html lang="en">
<head>
<meta charset="utf-8">
<title>Kelvarupath Presentation Folder</title>
<link href="https://fonts.googleapis.com/css2?family=Raleway:wght@300;400;600&display=swap" rel="stylesheet">
<style>
  :root {
    --orange: #f37122;
    --orange-deep: #d9511f;
    --charcoal: #26272a;
    --charcoal-dark: #1c1d1f;
    --ink: #000000;
    --paper: #ffffff;
    --stage: #5e5e5e;
    --muted: #c9c9c9;
  }
  * { box-sizing: border-box; margin: 0; padding: 0; }
  html, body {
    width: 816px; height: 1200px; overflow: hidden;
    background: var(--stage);
    font-family: "Raleway", sans-serif;
  }
  .canvas { position: relative; width: 816px; height: 1200px; }
  .spread {
    position: absolute; left: 28px; width: 760px; height: 537px;
    display: flex; box-shadow: 0 10px 30px rgba(0,0,0,.35);
  }
  .spread--outside { top: 30px; }
  .spread--inside { top: 620px; }
  .panel { position: relative; width: 380px; height: 537px; overflow: hidden; }

  .panel--dark {
    background: linear-gradient(135deg, var(--charcoal) 0%, #2f3033 45%, var(--charcoal-dark) 100%);
  }
  .panel--back { border-right: 1px solid rgba(255,255,255,.05); }

  .contact {
    position: absolute; left: 0; right: 0; top: 372px;
    text-align: center; color: var(--paper);
  }
  .brand-name {
    font-weight: 300; color: var(--paper); letter-spacing: -.5px;
  }
  .contact .brand-name { font-size: 22px; margin-bottom: 14px; }
  .contact-line { font-size: 10px; font-weight: 400; line-height: 1.35; }
  .contact-icon { display: block; margin: 7px auto 3px; }

  .tagline {
    position: absolute; top: 96px; right: 36px; width: 300px;
    text-align: center; color: var(--paper);
  }
  .tagline-lead { font-size: 20px; font-weight: 300; line-height: 1.2; }
  .tagline-close { font-size: 22px; font-weight: 600; margin-top: 6px; }
  .accent { color: var(--orange); }

  .front-brand {
    position: absolute; right: 30px; bottom: 78px; text-align: right;
  }
  .front-brand .brand-name { font-size: 24px; }
  .services { font-size: 6.5px; color: var(--muted); margin-top: 4px; letter-spacing: .2px; }

  .panel--white { background: var(--paper); }
  .panel--inside-right { background: linear-gradient(90deg, #ececec 0%, var(--paper) 18%); }
  .pocket--dark {
    position: absolute; left: 0; bottom: 0; width: 360px; height: 160px;
    background: linear-gradient(180deg, #2a2b2d, var(--charcoal-dark));
    border-top-right-radius: 22px;
  }
  .pocket--dark .brand-name {
    position: absolute; left: 34px; top: 44px; font-size: 34px;
  }
  .pocket--orange { position: absolute; left: 0; bottom: 0; }
</style>
</head>
<body>
<main class="canvas">
  <section class="spread spread--outside" aria-label="Folder outside">
    <div class="panel panel--dark panel--back" role="img" aria-label="Dark charcoal faceted triangle pattern background">
      <div class="contact">
        <p class="brand-name">Kelvarupath</p>
        <svg class="contact-icon" width="10" height="10" viewBox="0 0 10 10" aria-hidden="true"><path d="M2 1 L4 1 L4.6 3 L3.5 4 Q4.5 6 6 6.5 L7 5.4 L9 6 L9 8 Q5 9 2 5 Q1 3 2 1 Z" fill="var(--orange)"/></svg>
        <p class="contact-line">1300 482 917</p>
        <svg class="contact-icon" width="10" height="12" viewBox="0 0 10 12" aria-hidden="true"><path d="M5 0 A4 4 0 0 1 9 4 C9 7 5 12 5 12 C5 12 1 7 1 4 A4 4 0 0 1 5 0 Z" fill="var(--orange)"/><circle cx="5" cy="4" r="1.5" fill="var(--charcoal)"/></svg>
        <p class="contact-line">47 Tamsin Road<br>Brindlemoor, SA 5092</p>
        <svg class="contact-icon" width="10" height="10" viewBox="0 0 10 10" aria-hidden="true"><circle cx="5" cy="5" r="4.5" fill="var(--orange)"/></svg>
        <p class="contact-line">kelvarupath.com.au</p>
      </div>
    </div>
    <div class="panel panel--dark panel--front" role="img" aria-label="Dark charcoal faceted triangle pattern background">
      <div class="tagline">
        <p class="tagline-lead">Experience <span class="accent">finance</span> in a<br>whole new way...</p>
        <p class="tagline-close">Experience <span class="accent">Kelvarupath</span></p>
      </div>
      <div class="front-brand">
        <p class="brand-name">Kelvarupath</p>
        <p class="services">Asset Finance - Home Loans - Personal Loans</p>
      </div>
    </div>
  </section>

  <section class="spread spread--inside" aria-label="Folder inside">
    <div class="panel panel--white">
      <div class="pocket--dark">
        <p class="brand-name">Kelvarupath</p>
      </div>
    </div>
    <div class="panel panel--white panel--inside-right">
      <svg class="pocket--orange" width="380" height="180" viewBox="0 0 380 180" aria-hidden="true">
        <defs>
          <linearGradient id="pocketFill" x1="0" y1="0" x2="1" y2="0">
            <stop offset="0" stop-color="var(--orange-deep)"/>
            <stop offset="1" stop-color="var(--orange)"/>
          </linearGradient>
        </defs>
        <path d="M0 180 L40 24 Q46 4 66 4 L380 4 L380 180 Z" fill="url(#pocketFill)"/>
      </svg>
    </div>
  </section>
</main>
</body>
</html>
```